Banner

I need a banner made showcasing our products and USPs! I have attached a design that was done in-house but not very good so looking for a better design

Industry/Entity Type

Fintech

```html
<!DOCTYPE html>
<html lang="en">
<head>
<meta charset="utf-8">
<title>Clipwise Merchant Services – Banner</title>
<link href="https://fonts.googleapis.com/css2?family=Arvo:wght@700&family=Roboto:wght@400;500&family=Rokkitt:wght@700&display=swap" rel="stylesheet">
<style>
  :root {
    --navy: #1e3f86;
    --orange: #f08512;
    --grey-text: #6b6b6b;
    --rule: #d9dde3;
    --stage: #a8afb7;
    --white: #ffffff;
    --sky-top: #3f6fa8;
    --sky-bottom: #c7d8ea;
    --silver: #c9ccd1;
  }
  * { margin: 0; padding: 0; box-sizing: border-box; }
  html, body { width: 1200px; height: 1157px; overflow: hidden; background: var(--stage); }
  .stage { position: relative; width: 1200px; height: 1157px; }
  .banner {
    position: absolute; left: 319px; top: 20px;
    width: 611px; height: 1215px;
    background: var(--white);
    transform: scale(0.919); transform-origin: top left;
    font-family: "Roboto", Arial, sans-serif;
    overflow: hidden;
  }
  .shapes { position: absolute; inset: 0; }
  .brand-mark {
    position: absolute; left: 43px; top: 38px; width: 140px; height: 140px;
    border-radius: 50%; background: var(--navy); border: 5px solid var(--silver);
  }
  .brand-name {
    position: absolute; left: 205px; top: 36px;
    font-family: "Rokkitt", Georgia, serif; font-weight: 700;
    font-size: 96px; line-height: 1; color: var(--navy); letter-spacing: -1px;
  }
  .brand-tagline {
    position: absolute; left: 291px; top: 138px;
    font-size: 26px; color: var(--grey-text); letter-spacing: 0.2px;
  }
  .quote-tag {
    position: absolute; left: 38px; top: 228px; width: 170px;
    font-family: "Arvo", Georgia, serif; font-weight: 700;
    font-size: 20px; line-height: 27px; color: var(--navy); text-align: center;
  }
  .usp-list { position: absolute; left: 37px; top: 566px; width: 551px; list-style: none; }
  .usp-list li {
    height: 54px; padding-left: 95px; display: flex; align-items: center;
    font-size: 22px; color: var(--navy); border-bottom: 1px solid var(--rule);
  }
  .usp-list li:last-child { border-bottom: none; }
  .usp-list li::before {
    content: ""; width: 9px; height: 9px; border-radius: 50%;
    background: var(--navy); margin-right: 10px;
  }
  .services { position: absolute; left: 25px; top: 842px; width: 570px; display: flex; }
  .service { width: 190px; display: flex; flex-direction: column; align-items: center; position: relative; }
  .service + .service::before {
    content: ""; position: absolute; left: 0; top: 145px; width: 2px; height: 60px; background: var(--navy);
  }
  .service-icon {
    width: 138px; height: 138px; border-radius: 50%;
    background: var(--navy); border: 6px solid var(--silver);
  }
  .service-label { margin-top: 28px; font-size: 21px; color: var(--navy); white-space: nowrap; }
  .accepted {
    position: absolute; left: 52px; top: 1136px; width: 525px;
    display: flex; justify-content: space-between; align-items: center;
    list-style: none;
  }
  .accepted li {
    font-size: 17px; font-weight: 500; color: var(--white);
  }
</style>
</head>
<body>
<div class="stage">
  <div class="banner">
    <svg class="shapes" width="611" height="1215" viewBox="0 0 611 1215" aria-hidden="false">
      <defs>
        <linearGradient id="sky" x1="0" y1="0" x2="0" y2="1">
          <stop offset="0" stop-color="var(--sky-top)"/>
          <stop offset="1" stop-color="var(--sky-bottom)"/>
        </linearGradient>
      </defs>
      <polygon points="0,216 611,258 611,548 0,505" fill="url(#sky)" role="img" aria-label="Photograph looking up at glass skyscrapers against a blue sky"/>
      <polygon points="0,198 611,240 611,262 0,220" fill="var(--navy)"/>
      <polygon points="0,505 611,548 611,567 0,524" fill="var(--orange)"/>
      <polygon points="31,216 215,216 215,304 123,330 31,304" fill="var(--white)"/>
      <polygon points="0,1072 611,1125 611,1215 0,1215" fill="var(--orange)"/>
      <polygon points="110,1090 611,1063 611,1133" fill="var(--navy)"/>
    </svg>

    <div class="brand-mark" role="img" aria-label="Clipwise emblem"></div>
    <div class="brand-name">Clipwise</div>
    <div class="brand-tagline">Merchant Services</div>

    <p class="quote-tag">We will beat ANY like for like Quote</p>

    <ul class="usp-list">
      <li>SAME DAY/NEXT DAY FUNDING</li>
      <li>24 HOUR SWAP-OUT</li>
      <li>POCKET PAY &amp; TAP WALLET ENABLED</li>
      <li>INTERGRATED EPOS SOLUTION</li>
      <li>SAVE UP TO 40%</li>
    </ul>

    <div class="services">
      <div class="service">
        <div class="service-icon" role="img" aria-label="Card payment terminal"></div>
        <span class="service-label">CARD PAYMENTS</span>
      </div>
      <div class="service">
        <div class="service-icon" role="img" aria-label="Stack of banknotes"></div>
        <span class="service-label">CASH ADVANCE</span>
      </div>
      <div class="service">
        <div class="service-icon" role="img" aria-label="Touchscreen till with cash drawer"></div>
        <span class="service-label">EPOS SYSTEMS</span>
      </div>
    </div>

    <ul class="accepted" aria-label="Accepted payment methods">
      <li>Tap</li>
      <li>Vireo</li>
      <li>Meridia</li>
      <li>Orbicard</li>
      <li>Swivel</li>
      <li>Lumo</li>
      <li>Pocket Pay</li>
    </ul>
  </div>
</div>
</body>
</html>
```